Looking for an amazing business card for a thriving DJ business

We need a business card design for a DJ company based in South Florida. The DJ company specializes in weddings, parties, bar mitzvahs, corporate events, proms, and reunions. We are looking for a modern, simple business card design. The card should state DJ Marlow K.
Updates

The name on the card should be DJ Marlow K

Industry/Entity Type

Entertainment Industry

Contact Information for Business Card

DJ Marlow K
512.447.2086
atxdjmarlowk@quellmail.com
https://www.socialnook.com/DjMarlowK/
https://www.snapgrid.com/djmarlow.k/
www.djmarlowk.net

Font styles to use
Serif
Sans Serif

Requirements
Must have
• My business card has to be awesome.
Should not have
• The card has to have personality.

```html
<!DOCTYPE html>
<html lang="en">
<head>
<meta charset="utf-8">
<title>DJ Marlow K — Business Card</title>
<link href="https://fonts.googleapis.com/css2?family=Jost:wght@300;400;700&display=swap" rel="stylesheet">
<style>
  :root {
    --page: #f1f1f1;
    --kraft: #c99a51;
    --kraft-deep: #8a6a3a;
    --charcoal: #383838;
    --ink: #333333;
    --gold: #c99a51;
    --paper: #ffffff;
  }
  * { margin: 0; padding: 0; box-sizing: border-box; }
  html, body {
    width: 1200px; height: 1200px; overflow: hidden;
    background: var(--page);
    font-family: "Jost", "Futura", sans-serif;
  }
  .canvas { position: relative; width: 1200px; height: 1200px; }

  .card {
    position: absolute; left: 294px; width: 621px; height: 358px;
    overflow: hidden;
  }

  /* Front */
  .card-front { top: 177px; background: var(--kraft); }
  .front-title {
    position: absolute; left: 0; right: 0; top: 120px;
    text-align: center; color: var(--ink);
  }
  .front-name { font-size: 60px; line-height: 1; letter-spacing: 1px; }
  .front-name .prefix { font-weight: 700; }
  .front-name .given { font-weight: 300; }
  .front-url {
    margin-top: 2px; font-size: 22px; font-weight: 400;
    letter-spacing: 3px; line-height: 1.1;
  }
  .equalizer-band {
    position: absolute; left: 0; right: 0; bottom: 0; height: 110px;
    background: linear-gradient(to bottom, rgba(138,106,58,0) 0%, rgba(138,106,58,0.45) 100%);
  }

  /* Back */
  .card-back { top: 645px; background: var(--charcoal); color: var(--paper); }
  .contact { position: absolute; left: 48px; top: 47px; }
  .contact-name { font-size: 29px; font-weight: 700; color: var(--gold); line-height: 1.1; letter-spacing: 0.5px; }
  .contact-phone { font-size: 22px; font-weight: 300; line-height: 1.3; margin-top: 2px; }
  .contact-email { font-size: 19px; font-weight: 300; line-height: 1.3; margin-top: 2px; }

  .social { position: absolute; left: 44px; top: 216px; list-style: none; }
  .social li {
    display: flex; align-items: center; height: 35px;
    font-size: 19px; font-weight: 300;
  }
  .social .dot {
    width: 12px; height: 12px; border-radius: 50%;
    background: var(--gold); margin-right: 16px; margin-left: 2px;
  }

  .brand-mark {
    position: absolute; right: 44px; top: 74px;
    display: flex; align-items: center; gap: 8px;
  }
  .brand-mark .circle {
    width: 14px; height: 14px; border-radius: 50%; background: var(--gold);
  }
  .brand-mark .brand-name {
    font-size: 20px; font-weight: 400; color: var(--gold); letter-spacing: 1px;
  }

  .stripe { position: absolute; left: 0; right: 0; height: 4px; background: var(--gold); }
  .stripe-upper { top: 343px; }
  .stripe-lower { top: 354px; }
</style>
</head>
<body>
<main class="canvas">
  <section class="card card-front">
    <div class="front-title">
      <div class="front-name"><span class="prefix">DJ</span> <span class="given">Marlow K</span></div>
      <div class="front-url">www.djmarlowk.net</div>
    </div>
    <div class="equalizer-band" role="img" aria-label="Dotted audio equalizer bars rising from the bottom edge"></div>
  </section>

  <section class="card card-back">
    <div class="contact">
      <div class="contact-name">DJ Marlow K</div>
      <div class="contact-phone">512.447.2086</div>
      <div class="contact-email">atxdjmarlowk@quellmail.com</div>
    </div>

    <div class="brand-mark">
      <span class="circle"></span>
      <span class="brand-name">Nightbloom</span>
    </div>

    <ul class="social">
      <li><span class="dot"></span>https://www.socialnook.com/DjMarlowK/</li>
      <li><span class="dot"></span>https://www.snapgrid.com/djmarlow.k/</li>
    </ul>

    <div class="stripe stripe-upper"></div>
    <div class="stripe stripe-lower"></div>
  </section>
</main>
</body>
</html>
```